Broschüren-Design für Produzent von hochwertigen Verpackungs- und Präsentationslösungen
Zielgruppe
Wir produzieren hochwertige Verpackungs- und Präsentationslösungen.
Unsere Zielgruppe sind Firmen, welche kreative Premium-Packaging benötigt.
Aufgabenstellung
- Format: A4 hoch
- Umfang: 6 Seiten
- Falzart: Wickelfalz
- Design muss sehr hochwertig sein. Passend zu unseren Produktion (siehe Bilder)
- Wir möchten mit diesem Falzprospekt eine Übersicht über unsere Produkte generieren.
- Die Produkte sind bereits schon hochwertig fotografiert und müssen in einem anspruchsvollen Design in Szene gesetzt werden.
- Der Prospekt sollte die Kunden emotional berühren.
- Auf der Titelseite werden wir den Titel «High Performance Packaging» mit Folien prägen
- Seitenaufbau gemäss meiner Visualisierung (im Anhang)
- Bei jeder Produktkategorie möchte ich ein Grosses Übersichtsbild zusammen mit einem kurzen Text.
Ergänzend können noch weitere (passende) Bilder der jeweiligen Kategorie abgebildet werden.
Im Anhang finden Sie:
- Visualisierung des zu gestaltenden Prospekt
- Werbeflyer (zur Ansicht/Inspiration). In etwa so stellen wir uns das Design/Tonalität vor.
- Weitere passende Produktbilder können vorerst auf der Webseite unseres Produktionspartner (www.bogenhaus.de) entnommen werden.

```html
<!DOCTYPE html>
<html lang="de">
<head>
<meta charset="utf-8">
<title>Praemio Pack – Wickelfalz-Prospekt</title>
<link href="https://fonts.googleapis.com/css2?family=Playfair+Display:ital,wght@1,800;1,900&family=Barlow:wght@300;400;500&display=swap" rel="stylesheet">
<style>
:root{
  --page:#ffffff;
  --slate:#3e4250;
  --ink:#111214;
  --white:#ffffff;
  --soft:#d6d8de;
  --muted:#b9bcc6;
  --copper:#c4744c;
  --copper-light:#de9a72;
  --rule:#cfd2d9;
  --serif:"Playfair Display", Georgia, serif;
  --sans:"Barlow", Arial, sans-serif;
}
*{margin:0;padding:0;box-sizing:border-box}
html,body{width:1015px;height:1200px;overflow:hidden;background:var(--page)}
body{position:relative;font-family:var(--sans);color:var(--white)}

.brand-mark{position:absolute;top:96px;left:0;width:1015px;text-align:center;font-family:var(--sans);font-weight:500;font-size:20px;letter-spacing:1px;color:var(--ink)}
.brand-mark::before{content:"";display:inline-block;width:12px;height:12px;background:var(--ink);margin-right:8px;vertical-align:0}

.spread{position:absolute;left:36px;width:943px;height:446px;overflow:hidden;box-shadow:0 6px 22px rgba(0,0,0,.18)}
.spread-outer{top:221px;background:var(--slate)}
.spread-inner{top:691px;background:#2a2b30}

.fold{position:absolute;top:6px;bottom:6px;width:0;border-left:1px dashed rgba(255,255,255,.35)}

.panel{position:absolute;top:0;height:446px}
.panel-info{left:0;width:312px}
.headline{position:absolute;left:52px;top:46px;font-family:var(--serif);font-style:italic;font-weight:900;font-size:16px;line-height:19px;color:var(--white)}
.body-copy{position:absolute;left:52px;width:192px;font-weight:300;font-size:7px;line-height:9px;color:var(--soft)}
.body-copy p{margin-bottom:4px}
.subhead{position:absolute;left:52px;top:190px;font-weight:500;font-size:8.5px;line-height:11px;color:var(--white)}
.feature{position:absolute;left:53px;width:183px;height:44px}
.feature svg{position:absolute;left:0;top:0;width:34px;height:34px}
.feature h4{position:absolute;left:44px;top:1px;font-weight:500;font-size:7px;color:var(--white)}
.feature p{position:absolute;left:44px;top:14px;width:140px;font-weight:300;font-size:6.8px;line-height:9px;color:var(--soft)}
.feature-rule{position:absolute;left:53px;width:183px;border-top:1px solid var(--rule)}

.contact{position:absolute;left:518px;top:400px;display:flex;gap:6px;align-items:flex-start}
.contact-name{font-weight:500;font-size:7px;color:var(--white);padding-top:1px}
.contact-lines{font-size:4.2px;line-height:5.4px;color:var(--soft);font-weight:300}
.contact-lines strong{font-weight:500;color:var(--white)}
.contact-lines .maker{margin-top:4px}

.cover-photo{position:absolute;left:664px;top:66px;width:279px;height:166px;border-radius:2px;
  background:
    radial-gradient(ellipse 22% 40% at 22% 45%, #9a6448 0%, #7d4f38 55%, rgba(125,79,56,0) 100%),
    radial-gradient(ellipse 30% 22% at 64% 66%, #a7aab8 0%, #6f7280 55%, rgba(62,66,80,0) 100%),
    radial-gradient(ellipse 18% 18% at 94% 28%, #b9bcc8 0%, rgba(62,66,80,0) 100%),
    linear-gradient(180deg, #3e4250 0%, #35383f 70%, #3e4250 100%)}
.cover-title{position:absolute;left:666px;top:264px;font-family:var(--serif);font-style:italic;font-weight:900;font-size:31px;line-height:32px;color:var(--copper);background:linear-gradient(100deg,var(--copper),var(--copper-light) 45%,var(--copper));-webkit-background-clip:text;background-clip:text;-webkit-text-fill-color:transparent}
.cover-sub{position:absolute;left:666px;top:366px;font-weight:300;font-size:10px;line-height:13px;color:var(--soft)}

.tile{position:absolute;overflow:hidden}
.tile-photo{position:absolute;inset:0}
.caption{position:absolute;width:70px}
.caption h3{font-family:var(--serif);font-style:italic;font-weight:800;font-size:6.5px;color:var(--white);margin-bottom:4px}
.caption p{font-weight:300;font-size:3.9px;line-height:6.3px;color:var(--muted)}

.photo-packaging{background:
  radial-gradient(ellipse 28% 34% at 50% 48%, #ececee 0%, #b5b6ba 50%, rgba(20,20,22,0) 100%),
  radial-gradient(ellipse 18% 18% at 80% 30%, #c9cacd 0%, rgba(20,20,22,0) 100%),
  radial-gradient(ellipse 20% 22% at 86% 75%, #55565a 0%, rgba(20,20,22,0) 100%),
  linear-gradient(110deg,#111113 0%,#1f2022 60%,#18191b 100%)}
.photo-binder{background:
  radial-gradient(ellipse 42% 55% at 30% 62%, #45bfdc 0%, #2f97b2 50%, rgba(54,55,60,0) 100%),
  radial-gradient(ellipse 26% 28% at 66% 24%, #15191e 0%, rgba(54,55,60,0) 100%),
  radial-gradient(ellipse 16% 16% at 32% 32%, #e8eaec 0%, rgba(54,55,60,0) 100%),
  linear-gradient(160deg,#3a3b40 0%,#313237 100%)}
.photo-fan{background:
  radial-gradient(ellipse 30% 46% at 34% 45%, #b2b4c0 0%, #8a8c98 50%, rgba(45,46,50,0) 100%),
  radial-gradient(ellipse 30% 10% at 70% 92%, #a9abb6 0%, rgba(45,46,50,0) 100%),
  linear-gradient(160deg,#3a3b40 0%,#2b2c30 100%)}
.photo-folder{background:
  radial-gradient(ellipse 24% 28% at 26% 62%, #f0f0f2 0%, #9c9da1 50%, rgba(30,30,32,0) 100%),
  radial-gradient(ellipse 50% 55% at 38% 55%, #18181a 0%, rgba(44,45,48,0) 100%),
  linear-gradient(120deg,#35363a 0%,#27282b 100%)}
.photo-slipcase{background:
  radial-gradient(ellipse 14% 40% at 62% 35%, #1f1f23 0%, #2c2c31 55%, rgba(110,111,118,0) 100%),
  radial-gradient(ellipse 38% 20% at 55% 88%, #e6e6e8 0%, #b3b4ba 50%, rgba(110,111,118,0) 100%),
  radial-gradient(ellipse 18% 16% at 88% 62%, #dcdde0 0%, rgba(110,111,118,0) 100%),
  linear-gradient(160deg,#85868d 0%,#64656b 55%,#53545a 100%)}
.photo-case{background:
  radial-gradient(ellipse 30% 26% at 38% 30%, #4c4c50 0%, #2a2a2c 55%, rgba(12,12,13,0) 100%),
  radial-gradient(ellipse 32% 24% at 50% 68%, #303033 0%, rgba(12,12,13,0) 100%),
  radial-gradient(ellipse 20% 18% at 12% 85%, #222224 0%, rgba(12,12,13,0) 100%),
  linear-gradient(180deg,#1a1a1b 0%,#0c0c0d 100%)}
.photo-sample{background:
  radial-gradient(ellipse 20% 24% at 50% 70%, #f2f2f3 0%, #a6a7ab 50%, rgba(70,71,76,0) 100%),
  radial-gradient(ellipse 18% 20% at 78% 30%, #c4a488 0%, #8c735f 50%, rgba(70,71,76,0) 100%),
  radial-gradient(ellipse 40% 40% at 55% 60%, #1e1e20 0%, rgba(70,71,76,0) 100%),
  linear-gradient(130deg,#56575c 0%,#45464b 100%)}
.photo-writing{background:
  radial-gradient(ellipse 22% 26% at 46% 46%, #f0f0f2 0%, #a2a3a7 50%, rgba(60,61,66,0) 100%),
  radial-gradient(ellipse 22% 18% at 72% 22%, #7a7b80 0%, rgba(60,61,66,0) 100%),
  radial-gradient(ellipse 44% 40% at 40% 55%, #1c1c1e 0%, rgba(60,61,66,0) 100%),
  linear-gradient(150deg,#2a2b2f 0%,#4a4b50 100%)}
</style>
</head>
<body>

<div class="brand-mark">Praemio Pack</div>

<section class="spread spread-outer">
  <div class="fold" style="left:312px"></div>
  <div class="fold" style="left:628px"></div>

  <div class="panel panel-info">
    <h2 class="headline">Höchste Qualität zu<br>unschlagbaren Preisen.</h2>
    <div class="body-copy" style="top:102px">
      <p>Mit einer unvergleichlich grossen Bandbreite im Bereich des Premium Packaging bieten wir vielseitige Verpackungs- und Präsentationslösungen.</p>
      <p>Einzigartiges Design, variable Formen und hochwertige Haptik unterstreichen die Bedeutung von Ihren Produkten.</p>
      <p>Überzeugen Sie sich jetzt und bestellen Sie<br>Ihr individuelles Angebot!</p>
    </div>
    <h3 class="subhead">Nachhaltige Papiere<br>als Standard.</h3>
    <div class="body-copy" style="top:218px;width:190px">
      <p>Bei uns gehen neuste Technologien und Umweltschutz Hand in Hand. Wir setzen auf nachhaltige Materialien und eine emissionsarme Produktion.</p>
    </div>

    <div class="feature" style="top:266px">
      <svg viewBox="0 0 34 34" fill="none" stroke="#fff" stroke-width="1">
        <path d="M4 26 L10 12 L16 26 Z M12 26 L19 8 L26 26 Z M20 26 L26 14 L32 26 Z"/>
        <path d="M10 26v4 M19 26v4 M26 26v4 M2 30h31"/>
      </svg>
      <h4>Nachhaltige Papiere</h4>
      <p>Unsere Rohmaterialien stammen aus nachhaltiger Forstwirtschaft.</p>
    </div>
    <div class="feature-rule" style="top:305px"></div>

    <div class="feature" style="top:315px">
      <svg viewBox="0 0 34 34" fill="none" stroke="#fff" stroke-width="1.2">
        <path d="M17 2 L29 7 V17 C29 25 23 30 17 32 C11 30 5 25 5 17 V7 Z"/>
        <path d="M11.5 17 L15.5 21 L22.5 13" stroke-width="2"/>
      </svg>
      <h4>Wiederverwendbarkeit</h4>
      <p>Unsere Boxen sind so schön und stabil, dass man sie auf jeden Fall wiederverwendet.</p>
    </div>
    <div class="feature-rule" style="top:356px"></div>

    <div class="feature" style="top:364px">
      <svg viewBox="0 0 34 34" fill="none" stroke="#fff" stroke-width="1">
        <path d="M10 9 A11 11 0 0 1 28 14 M28 14 l1-4 M28 14 l-4-1"/>
        <path d="M27 25 A11 11 0 0 1 8 25 M8 25 l0 4 M8 25 l4 0"/>
        <path d="M6 19 A11 11 0 0 1 10 9 M10 9 l-4 0 M10 9 l0 4"/>
        <circle cx="17" cy="18" r="6"/>
        <path d="M14 17 a3 3 0 0 1 5-1 M20 19 a3 3 0 0 1-5 1"/>
      </svg>
      <h4>Recyclebare Lösungen</h4>
      <p>Auf Nachfrage können wir Ihnen eine 100% recyclebare Verpackung anbieten.</p>
    </div>
  </div>

  <div class="contact">
    <span class="contact-name">Praemio Pack</span>
    <div class="contact-lines">
      <strong>praemio-pack.ch</strong><br>
      info@praemio-pack.ch<br>
      041 555 27 90
      <div class="maker">Eine Marke von FalterPresse AG</div>
    </div>
  </div>

  <div class="cover-photo" role="img" aria-label="Produktfoto: kupferfarbener Schuber und dunkle Schubladenbox mit grauen Schubladen"></div>
  <h1 class="cover-title">High<br>Performance<br>Packaging</h1>
  <p class="cover-sub">Exklusive Verpackungs-<br>und Präsentationslösungen</p>
</section>

<section class="spread spread-inner">
  <div class="tile" style="left:0;top:0;width:315px;height:149px">
    <div class="tile-photo photo-packaging" role="img" aria-label="Produktfoto: weisse Klappschachtel mit Stift und silberne Geschenkbox"></div>
    <div class="caption" style="left:19px;top:76px"><h3>Verpackungen.</h3><p>Massgefertigte Lösungen aus edlen Materialien, präzise verarbeitet und individuell veredelt. Jedes Detail unterstreicht den Wert Ihrer Produkte und hinterlässt einen bleibenden Eindruck bei Ihren Kunden.</p></div>
  </div>
  <div class="tile" style="left:315px;top:0;width:316px;height:149px">
    <div class="tile-photo photo-binder" role="img" aria-label="Produktfoto: aufgeklappter Ringordner mit türkisfarbenem Innenbezug"></div>
    <div class="caption" style="left:222px;top:75px"><h3>Ringordner.</h3><p>Massgefertigte Lösungen aus edlen Materialien, präzise verarbeitet und individuell veredelt. Jedes Detail unterstreicht den Wert Ihrer Produkte und hinterlässt einen bleibenden Eindruck bei Ihren Kunden.</p></div>
  </div>
  <div class="tile" style="left:631px;top:0;width:312px;height:223px">
    <div class="tile-photo photo-fan" role="img" aria-label="Produktfoto: graue Fächermappe mit Registern"></div>
    <div class="caption" style="left:203px;top:32px"><h3>Fächermappen.</h3><p>Massgefertigte Lösungen aus edlen Materialien, präzise verarbeitet und individuell veredelt. Jedes Detail unterstreicht den Wert Ihrer Produkte und hinterlässt einen bleibenden Eindruck bei Ihren Kunden.</p></div>
  </div>
  <div class="tile" style="left:0;top:149px;width:315px;height:151px">
    <div class="tile-photo photo-folder" role="img" aria-label="Produktfoto: schwarze Präsentationsmappe mit Papierbogen"></div>
    <div class="caption" style="left:222px;top:47px"><h3>Präsentationsmappen.</h3><p>Massgefertigte Lösungen aus edlen Materialien, präzise verarbeitet und individuell veredelt. Jedes Detail unterstreicht den Wert Ihrer Produkte und hinterlässt einen bleibenden Eindruck bei Ihren Kunden.</p></div>
  </div>
  <div class="tile" style="left:315px;top:149px;width:316px;height:151px">
    <div class="tile-photo photo-slipcase" role="img" aria-label="Produktfoto: Schuber mit drei Ordnern und Farbmusterkarten"></div>
    <div class="caption" style="left:36px;top:47px"><h3>Schuber.</h3><p>Massgefertigte Lösungen aus edlen Materialien, präzise verarbeitet und individuell veredelt. Jedes Detail unterstreicht den Wert Ihrer Produkte und hinterlässt einen bleibenden Eindruck bei Ihren Kunden.</p></div>
  </div>
  <div class="tile" style="left:631px;top:223px;width:312px;height:223px">
    <div class="tile-photo photo-case" role="img" aria-label="Produktfoto: schwarzer Präsentationskoffer mit Schaumstoffeinlage"></div>
    <div class="caption" style="left:203px;top:41px"><h3>Präsentationskoffer.</h3><p>Massgefertigte Lösungen aus edlen Materialien, präzise verarbeitet und individuell veredelt. Jedes Detail unterstreicht den Wert Ihrer Produkte und hinterlässt einen bleibenden Eindruck bei Ihren Kunden.</p></div>
  </div>
  <div class="tile" style="left:0;top:300px;width:315px;height:146px">
    <div class="tile-photo photo-sample" role="img" aria-label="Produktfoto: Mustermappe mit Holzmustern"></div>
    <div class="caption" style="left:19px;top:18px"><h3>Mustermappen.</h3><p>Massgefertigte Lösungen aus edlen Materialien, präzise verarbeitet und individuell veredelt. Jedes Detail unterstreicht den Wert Ihrer Produkte und hinterlässt einen bleibenden Eindruck bei Ihren Kunden.</p></div>
  </div>
  <div class="tile" style="left:315px;top:300px;width:316px;height:146px">
    <div class="tile-photo photo-writing" role="img" aria-label="Produktfoto: Schreibmappe mit Schreibblock und Stift"></div>
    <div class="caption" style="left:222px;top:76px"><h3>Schreibmappen.</h3><p>Massgefertigte Lösungen aus edlen Materialien, präzise verarbeitet und individuell veredelt. Jedes Detail unterstreicht den Wert Ihrer Produkte und hinterlässt einen bleibenden Eindruck bei Ihren Kunden.</p></div>
  </div>
</section>

</body>
</html>
```